RidgeHornSupply.com

I need a new webdesign for a company in the San Jose/SF Bay area that showcases the financial benefits of buying used band instruments for junior high students.This would be opposed to the current and costly option of renting cheap quality instruments from the 2 or 3 local music stores that charge a monthly fee that over the years charges the buyer 3 or 4x over..
Instruments: focus in on Alto Sax, Trumpet, Flute, Clarinet, Trombone, Tenor Sax, Baritone
Target middle schools are Kestrelwood Middle School and Harlow Middle School in San Jose, CA. Both have award winning band programs.
Files attached may or may not be important.
Tabs Needed and funtional
Contact
Shopping Cart
Select Instrument
Checkout
Add to Cart, etc.
Instuments
quantity, etc.
trade in your instrument/sell your instrument
ability to add or take away new instruments for sale. including pictures
Additional questions or info, feel free to ask
Hi Designers,
Project Deadline Extended
Reason: In the next week you will be receiving specific content that will be required to be had on the website.
New desigins are still welcome. Please continue to contact me if you have questions about your individual designs.
Thanks!
Ridge Horn

```html
<!DOCTYPE html>
<html lang="en">
<head>
<meta charset="utf-8">
<title>Ridge Horn Instruments</title>
<link href="https://fonts.googleapis.com/css2?family=Open+Sans:wght@400;600;700&display=swap" rel="stylesheet">
<style>
:root{
  --blue:#0a8ee0;
  --blue-dark:#0770c2;
  --red:#c8141b;
  --ink:#222;
  --muted:#999;
  --bar:#2b2b2b;
  --footer:#444;
  --footer-bottom:#2d2d2d;
  --footer-text:#bdbdbd;
  --page:#f1f1f1;
  --line:#dcdcdc;
}
*{box-sizing:border-box;margin:0;padding:0}
html,body{width:1065px;height:1200px;overflow:hidden}
body{font-family:"Open Sans",Arial,sans-serif;background:var(--page);color:var(--ink);position:relative}
a{color:inherit;text-decoration:none}
.wrap{width:869px;margin:0 auto;position:relative}

.top-bar{height:31px;background:var(--bar)}
.top-links{display:flex;justify-content:flex-end;gap:20px;font-size:10px;color:#fff;line-height:31px}

.header{height:111px;background:linear-gradient(#f4f4f4,#e6e6e6)}
.header .wrap{height:111px}
.brand{position:absolute;left:0;top:29px;font-size:27px;font-weight:700;color:var(--blue);line-height:30px;letter-spacing:.3px}
.brand-sub{position:absolute;left:0;top:62px;font-size:22px;color:var(--red);line-height:26px}
.phone{position:absolute;right:0;top:23px;font-size:21px;font-weight:700;color:var(--muted)}
.search{position:absolute;left:439px;top:62px;width:220px;height:28px;background:#fff;border:1px solid #ddd;font-size:11px;color:#999;padding:6px 11px}
.search-btn{position:absolute;left:651px;top:57px;width:35px;height:35px;border-radius:50%;background:var(--blue);display:flex;align-items:center;justify-content:center}
.cart-btn{position:absolute;left:699px;top:57px;width:35px;height:35px;border-radius:50%;background:var(--red);display:flex;align-items:center;justify-content:center}
.cart-summary{position:absolute;left:741px;top:67px;font-size:11px}
.cart-summary .total{color:var(--red)}
.cart-summary .checkout{color:var(--blue);margin-left:3px}

.nav{height:38px;background:linear-gradient(#e3e3e3,#fafafa 55%,#f3f3f3);border-bottom:1px solid var(--line)}
.nav ul{list-style:none;display:flex;font-size:12px;line-height:38px;color:#222}
.nav li+li::before{content:"";display:inline-block;width:1px;height:9px;background:#bbb;margin:0 10px;vertical-align:middle}

.hero{margin-top:13px;height:305px;border:1px solid #ddd;border-radius:3px;background:radial-gradient(ellipse at 75% 40%,#fafafa,#e2e2e2 80%);position:relative;overflow:hidden}
.hero h1{position:absolute;left:40px;top:94px;font-size:27px;font-weight:700;letter-spacing:-.3px}
.hero h1 span{color:var(--red)}
.hero p{position:absolute;left:41px;top:135px;width:380px;font-size:12.5px;line-height:18px;color:#444}
.buy{position:absolute;left:42px;top:203px;background:var(--blue);color:#fff;font-size:12px;padding:4px 15px;border-radius:2px}
.dots{position:absolute;left:45px;top:267px;display:flex;gap:5px}
.dots i{width:11px;height:11px;border-radius:50%;background:#777}
.dots i:first-child{background:#222}
.hero-art{position:absolute;left:450px;top:18px;width:390px;height:270px;background:radial-gradient(ellipse at 60% 55%,#e4bf5c,#d6a93a 30%,rgba(230,230,230,0) 70%);opacity:.75}

.section-title{text-align:center;font-size:21px;font-weight:400;color:#333;margin-top:17px;line-height:26px}
.grid{margin-top:12px;display:grid;grid-template-columns:repeat(4,209px);gap:11px 11px;justify-content:space-between}
.card{height:208px;background:#fff;border:1px solid #ddd;border-radius:2px;position:relative;text-align:center}
.card .thumb{position:absolute;left:35px;top:20px;width:138px;height:110px;border-radius:4px}
.thumb.brass{background:radial-gradient(ellipse,#d9b24f,#f4e7c2 55%,#fff 80%)}
.thumb.wood{background:radial-gradient(ellipse,#c98a45,#f2dcc3 40%,#fff 75%)}
.thumb.black{background:radial-gradient(ellipse,#3a3a3a,#cfcfcf 40%,#fff 75%)}
.card .name{position:absolute;left:0;right:0;top:143px;font-size:12.5px;color:#333}
.card .price{color:var(--red);font-weight:700;margin-left:6px}
.add{position:absolute;left:48px;top:168px;width:113px;height:24px;background:var(--blue);color:#fff;font-size:12.5px;border-radius:2px;display:flex;align-items:center;justify-content:center;gap:9px}
.row2 .name{top:142px}
.row2 .add{top:171px}

.footer{position:absolute;left:0;top:1007px;width:1065px;height:154px;background:var(--footer)}
.footer .wrap{height:154px}
.col{position:absolute;top:14px}
.col h4{font-size:12.5px;font-weight:700;color:#fff;margin-bottom:10px}
.col ul{list-style:none;font-size:11px;color:var(--footer-text);line-height:20.5px}
.social li{display:flex;align-items:center;gap:10px;line-height:32px;color:#fff}
.social i{width:29px;height:29px;border-radius:50%;background:#ddd;display:block}
.legal{position:absolute;left:0;top:1161px;width:1065px;height:39px;background:var(--footer-bottom);color:#aaa;font-size:9px;text-align:center;line-height:36px}
</style>
</head>
<body>

<div class="top-bar">
  <div class="wrap top-links">
    <a href="#">Login</a><a href="#">Signup</a><a href="#">My Account</a><a href="#">Order Status</a><a href="#">Wish List</a>
  </div>
</div>

<header class="header">
  <div class="wrap">
    <div class="brand">Ridge Horn</div>
    <div class="brand-sub">Instruments</div>
    <div class="phone">(800) 555-0142</div>
    <div class="search">Product Search</div>
    <div class="search-btn">
      <svg width="15" height="15" viewBox="0 0 16 16"><circle cx="6.5" cy="6.5" r="4.8" fill="none" stroke="#fff" stroke-width="2"/><line x1="10" y1="10" x2="14.5" y2="14.5" stroke="#fff" stroke-width="2.2" stroke-linecap="round"/></svg>
    </div>
    <div class="cart-btn">
      <svg width="20" height="16" viewBox="0 0 20 16"><path d="M1 2h3l2 8h10l2-6H5" fill="none" stroke="#fff" stroke-width="2"/><circle cx="8" cy="14" r="1.5" fill="#fff"/><circle cx="15" cy="14" r="1.5" fill="#fff"/></svg>
    </div>
    <div class="cart-summary">0Items <span class="total">($0.00)</span> <a class="checkout" href="#">Checkout</a></div>
  </div>
</header>

<nav class="nav">
  <div class="wrap">
    <ul>
      <li>HOME</li><li>ABOUT US</li><li>PRODUCTS</li><li>SALE</li><li>SELECT INSTRUMENT</li><li>INSTUMENTS</li><li>QUANTITY</li><li>CONTACT US</li>
    </ul>
  </div>
</nav>

<main class="wrap">
  <section class="hero">
    <h1>BAND <span>INSTRUMENTS</span></h1>
    <p>Lorem Ipsum is simply dummy text of the printing and typesetting industry. Lorem Ipsum has been the industry's standard dummy text ever since the 1500s</p>
    <a class="buy" href="#">Buy Now</a>
    <div class="dots"><i></i><i></i><i></i></div>
    <div class="hero-art" role="img" aria-label="Photo of two gold trumpets"></div>
  </section>

  <h2 class="section-title">Featured Products</h2>

  <div class="grid">
    <div class="card"><div class="thumb brass" role="img" aria-label="Alto saxophone photo"></div><div class="name">Alto Sax <span class="price">($100)</span></div><a class="add" href="#"><svg width="18" height="14" viewBox="0 0 20 16"><path d="M1 2h3l2 8h10l2-6H5" fill="none" stroke="#fff" stroke-width="2"/><circle cx="8" cy="14" r="1.5" fill="#fff"/><circle cx="15" cy="14" r="1.5" fill="#fff"/></svg>Add to Cart</a></div>
    <div class="card"><div class="thumb brass" role="img" aria-label="Trumpet photo"></div><div class="name">Trumpet <span class="price">($100)</span></div><a class="add" href="#"><svg width="18" height="14" viewBox="0 0 20 16"><path d="M1 2h3l2 8h10l2-6H5" fill="none" stroke="#fff" stroke-width="2"/><circle cx="8" cy="14" r="1.5" fill="#fff"/><circle cx="15" cy="14" r="1.5" fill="#fff"/></svg>Add to Cart</a></div>
    <div class="card"><div class="thumb wood" role="img" aria-label="Wooden flute photo"></div><div class="name">Flute <span class="price">($100)</span></div><a class="add" href="#"><svg width="18" height="14" viewBox="0 0 20 16"><path d="M1 2h3l2 8h10l2-6H5" fill="none" stroke="#fff" stroke-width="2"/><circle cx="8" cy="14" r="1.5" fill="#fff"/><circle cx="15" cy="14" r="1.5" fill="#fff"/></svg>Add to Cart</a></div>
    <div class="card"><div class="thumb black" role="img" aria-label="Clarinet photo"></div><div class="name">Clarinet <span class="price">($100)</span></div><a class="add" href="#"><svg width="18" height="14" viewBox="0 0 20 16"><path d="M1 2h3l2 8h10l2-6H5" fill="none" stroke="#fff" stroke-width="2"/><circle cx="8" cy="14" r="1.5" fill="#fff"/><circle cx="15" cy="14" r="1.5" fill="#fff"/></svg>Add to Cart</a></div>

    <div class="card row2"><div class="thumb brass" role="img" aria-label="Alto saxophone photo"></div><div class="name">Alto Sax <span class="price">($100)</span></div><a class="add" href="#"><svg width="18" height="14" viewBox="0 0 20 16"><path d="M1 2h3l2 8h10l2-6H5" fill="none" stroke="#fff" stroke-width="2"/><circle cx="8" cy="14" r="1.5" fill="#fff"/><circle cx="15" cy="14" r="1.5" fill="#fff"/></svg>Add to Cart</a></div>
    <div class="card row2"><div class="thumb brass" role="img" aria-label="Trumpet photo"></div><div class="name">Trumpet <span class="price">($100)</span></div><a class="add" href="#"><svg width="18" height="14" viewBox="0 0 20 16"><path d="M1 2h3l2 8h10l2-6H5" fill="none" stroke="#fff" stroke-width="2"/><circle cx="8" cy="14" r="1.5" fill="#fff"/><circle cx="15" cy="14" r="1.5" fill="#fff"/></svg>Add to Cart</a></div>
    <div class="card row2"><div class="thumb wood" role="img" aria-label="Wooden flute photo"></div><div class="name">Flute <span class="price">($100)</span></div><a class="add" href="#"><svg width="18" height="14" viewBox="0 0 20 16"><path d="M1 2h3l2 8h10l2-6H5" fill="none" stroke="#fff" stroke-width="2"/><circle cx="8" cy="14" r="1.5" fill="#fff"/><circle cx="15" cy="14" r="1.5" fill="#fff"/></svg>Add to Cart</a></div>
    <div class="card row2"><div class="thumb black" role="img" aria-label="Clarinet photo"></div><div class="name">Clarinet <span class="price">($100)</span></div><a class="add" href="#"><svg width="18" height="14" viewBox="0 0 20 16"><path d="M1 2h3l2 8h10l2-6H5" fill="none" stroke="#fff" stroke-width="2"/><circle cx="8" cy="14" r="1.5" fill="#fff"/><circle cx="15" cy="14" r="1.5" fill="#fff"/></svg>Add to Cart</a></div>
  </div>
</main>

<footer class="footer">
  <div class="wrap">
    <div class="col" style="left:0"><h4>Order Info</h4><ul><li>How to Order</li><li>My Account</li><li>Order Status</li><li>Shipping</li><li>Policies &amp; Guarantees</li></ul></div>
    <div class="col" style="left:145px;top:44px"><ul><li>Warranties</li><li>Contact Us</li></ul></div>
    <div class="col" style="left:272px"><h4>Additional Info</h4><ul><li>Tech Support</li><li>Learning Center</li><li>Shopping Cart</li><li>Instuments</li><li>Affiliate Program</li></ul></div>
    <div class="col" style="left:408px;top:44px"><ul><li>Reseller Program</li><li>Privacy Policy</li><li>Terms of Use</li><li>Sitemap</li></ul></div>
    <div class="col" style="left:571px"><h4>About Us</h4><ul><li>About Us</li><li>Careers</li><li>Blog</li><li>Press</li><li>Online Shopping</li></ul></div>
    <div class="col" style="left:751px"><h4>Follow Us</h4><ul class="social"><li><i></i>Circlepage</li><li><i></i>Chirpline</li><li><i></i>ClipStream</li></ul></div>
  </div>
</footer>
<div class="legal">© 2014 RidgeHornSupply.com. All Right Reserved</div>

</body>
</html>
```